Stationery & Logo | PeakHaven - Swim Bike + Run Holidays in the Alps

About PeakHaven

PeakHaven create inspirational swimming, cycling, running and triathlon holidays in the Swiss Alps and we need a designer to create an inspirational look and feel for our new company.

PeakHaven guests will step off the rat race treadmill, slow down and revel in swimming, cycling or running in the beautiful Swiss countryside.

PeakHaven training holidays: fitter, happier and in love with your sport. Guaranteed.

Detailed design brief attached (Word version has hyperlinks, PDF is smaller).

Deliverables

Logo
Letterhead
Word template
A5 Flyer template
See specific requirements in attached design brief

Requirements
Must have
• Minimalist, clean, white space design

A logo that is text based with the company name featured

Handwriting style font for company name

Handwriting font that is slanty, curvy and sexy but still nice and readable

Web logo that is small in terms of KB for quick page load speed

See look and feel and mood boards in attached design brief
Nice to have
• Logo could have
Images of swim, bike, run in Swiss decoupage style
Images of mountain ranges, Swiss flag

But I want to keep it clean and minimal
Open to ideas and interpretation of the detailed creative brief attached
Should not have
• Things we are not

A bootcamp for very serious extreme athletes who don’t enjoy a glass of wine
Male dominated

```html
<!DOCTYPE html>
<html lang="en">
<head>
<meta charset="utf-8">
<title>PeakHaven – Stationery &amp; Logo</title>
<link href="https://fonts.googleapis.com/css2?family=Mulish:wght@300;400;700;800&display=swap" rel="stylesheet">
<style>
  :root{
    --brand-red:#e3262b;
    --brand-red-dark:#c81d22;
    --heading-muted:#9b2b2e;
    --paper:#ffffff;
    --board:#ffffff;
    --ink-grey:#8a8a8a;
    --photo-sky:#9ec3e0;
    --photo-mountain:#5f7a86;
    --photo-field:#6f9a3e;
  }
  *{box-sizing:border-box;margin:0;padding:0}
  html,body{width:1200px;height:750px;overflow:hidden;background:var(--board)}
  body{font-family:'Mulish',sans-serif;position:relative}

  /* brand lockup */
  .brand{position:absolute;text-align:center;color:var(--brand-red)}
  .brand__name{font-weight:300;letter-spacing:.01em;line-height:1;display:block;white-space:nowrap}
  .brand__tagline{font-weight:300;display:block;line-height:1;white-space:nowrap}

  .brand--hero{left:0;width:1200px;top:68px}
  .brand--hero .brand__name{font-size:64px}
  .brand--hero .brand__tagline{font-size:17px;margin-top:14px}

  .brand--letter{left:34px;top:46px;width:110px}
  .brand--letter .brand__name{font-size:24px}
  .brand--letter .brand__tagline{font-size:7px;margin-top:5px}

  .brand--card{left:0;width:104px;top:44px}
  .brand--card .brand__name{font-size:17px}
  .brand--card .brand__tagline{font-size:5.5px;margin-top:4px}

  .brand--flyer-back{left:22px;top:38px;width:74px;color:#fff}
  .brand--flyer-back .brand__name{font-size:15px}
  .brand--flyer-back .brand__tagline{font-size:4.8px;margin-top:3px}

  /* sheets */
  .sheet{position:absolute;background:var(--paper);box-shadow:0 0 5px rgba(0,0,0,.22)}
  .letterhead{top:175px;width:382px;height:541px}
  .letterhead--first{left:14px}
  .letterhead--continuation{left:405px}

  .contact{position:absolute;right:30px;top:29px;text-align:right;color:var(--ink-grey);font-size:4.4px;line-height:1.35}
  .contact__label{font-weight:700;font-size:4.6px;margin-top:6px;letter-spacing:.03em}
  .contact__label:first-child{margin-top:0}

  .letter-footer{position:absolute;left:0;right:0;top:521px;font-size:4.6px;color:var(--ink-grey)}
  .letter-footer span{position:absolute;transform:translateX(-50%);white-space:nowrap}

  /* flyers */
  .flyer{position:absolute;left:812px;width:373px;background:var(--brand-red);overflow:hidden;color:#fff}
  .flyer--front{top:175px;height:265px}
  .flyer--back{top:452px;height:264px;background:linear-gradient(135deg,#e5292e 0%,#e3262b 45%,#ea4246 70%,#e3262b 100%)}

  .flyer__rule{position:absolute;left:0;right:0;height:2px;background:#fff}

  .flyer__photo{position:absolute;left:0;top:16px;width:268px;height:232px;
    background:linear-gradient(180deg,var(--photo-sky) 0%,#c9dcea 22%,var(--photo-mountain) 40%,#6e8a5a 62%,var(--photo-field) 78%,#8a8c86 100%)}
  .flyer__panel{position:absolute;left:258px;top:16px;width:130px;height:232px;background:var(--brand-red-dark);border-top-left-radius:28px;border-bottom-left-radius:10px}
  .flyer__card{position:absolute;left:266px;top:13px;width:120px;height:116px;background:#fff;border-radius:14px;box-shadow:0 2px 4px rgba(0,0,0,.2)}

  .copy{position:absolute;width:88px}
  .copy__heading{font-size:8px;font-weight:800;color:var(--heading-muted);letter-spacing:.02em;margin-bottom:5px}
  .copy__heading b{color:#fff}
  .copy__text{font-size:4.7px;line-height:2.05}

  .flyer__url-tab{position:absolute;left:250px;top:232px;width:110px;height:40px;border:2px solid #fff;border-radius:10px;background:var(--brand-red);
    font-size:6.5px;font-weight:800;letter-spacing:.02em;text-align:center;padding-top:10px}
</style>
</head>
<body>

  <div class="brand brand--hero">
    <span class="brand__name">PeakHaven</span>
    <span class="brand__tagline">Alpine Training Holidays</span>
  </div>

  <section class="sheet letterhead letterhead--first">
    <div class="brand brand--letter">
      <span class="brand__name">PeakHaven</span>
      <span class="brand__tagline">Alpine Training Holidays</span>
    </div>
    <div class="contact">
      <div class="contact__label">ADRESS</div>
      <div>Chemin des Sapins 14</div>
      <div>1800 Vevey, Switzerland</div>
      <div class="contact__label">TELEPHONE</div>
      <div>m: +41 (0)21 555 0142</div>
      <div>p: +41 (0)21 555 0188</div>
      <div class="contact__label">WEB</div>
      <div>www.socialpage.net/PeakHaven</div>
      <div>Social: @PeakHaven</div>
      <div>hello@peakhaven.com</div>
      <div>www.peakhaven.com</div>
    </div>
  </section>

  <section class="sheet letterhead letterhead--continuation">
    <div class="brand brand--letter">
      <span class="brand__name">PeakHaven</span>
      <span class="brand__tagline">Alpine Training Holidays</span>
    </div>
    <div class="letter-footer">
      <span style="left:80px">www.peakhaven.com</span>
      <span style="left:187px">Social: @PeakHaven</span>
      <span style="left:298px">www.socialpage.net/PeakHaven</span>
    </div>
  </section>

  <section class="flyer flyer--front">
    <div class="flyer__rule" style="top:11px"></div>
    <div class="flyer__photo" role="img" aria-label="Photograph of a group of road cyclists riding past green fields toward snow-capped Alpine mountains"></div>
    <div class="flyer__panel"></div>
    <div class="flyer__rule" style="top:250px"></div>
    <div class="flyer__card">
      <div class="brand brand--card">
        <span class="brand__name">PeakHaven</span>
        <span class="brand__tagline">Alpine Training Holidays</span>
      </div>
    </div>
    <div class="copy" style="left:274px;top:140px">
      <div class="copy__heading">HEADING <b>01</b></div>
      <p class="copy__text">Lorem ipsum dolor sit amet, consectetur adipisicing elit, sed do eiusmod tempor incididunt ut labore et dolore magna aliqua. Ut enim ad minim veniam, quis nostrud exercitation ullamco laboris nisi ut aliquip ex ea commodo consequat.</p>
    </div>
  </section>

  <section class="flyer flyer--back">
    <div class="flyer__rule" style="top:11px"></div>
    <div class="brand brand--flyer-back">
      <span class="brand__name">PeakHaven</span>
      <span class="brand__tagline">Alpine Training Holidays</span>
    </div>
    <div class="copy" style="left:37px;top:104px">
      <div class="copy__heading">HEADING <b>01</b></div>
      <p class="copy__text">Lorem ipsum dolor sit amet, consectetur adipisicing elit, sed do eiusmod tempor incididunt ut labore et dolore magna aliqua. Ut enim ad minim veniam, quis nostrud exercitation ullamco laboris nisi ut aliquip ex ea commodo consequat.</p>
    </div>
    <div class="copy" style="left:157px;top:104px">
      <div class="copy__heading">HEADING <b>02</b></div>
      <p class="copy__text">Lorem ipsum dolor sit amet, consectetur adipisicing elit, sed do eiusmod tempor incididunt ut labore et dolore magna aliqua. Ut enim ad minim veniam, quis nostrud exercitation ullamco laboris nisi ut aliquip ex ea commodo consequat.</p>
    </div>
    <div class="copy" style="left:277px;top:104px">
      <div class="copy__heading">HEADING <b>03</b></div>
      <p class="copy__text">Lorem ipsum dolor sit amet, consectetur adipisicing elit, sed do eiusmod tempor incididunt ut labore et dolore magna aliqua. Ut enim ad minim veniam, quis nostrud exercitation ullamco laboris nisi ut aliquip ex ea commodo consequat.</p>
    </div>
    <div class="flyer__rule" style="top:249px"></div>
    <div class="flyer__url-tab">WWW.PEAKHAVEN.COM</div>
  </section>

</body>
</html>
```